App-Design für IT-Sicherheitsfirma
Zielgruppe
Wir sind eine IT-Sicherheitsfirma und suchen ein funktionelles und schlankes App Design.
Unsere Nutzer sind Mitarbeiter von international agierenden Konzernen. Die Zielgruppe sind international agierende Konzerne.
Die App gibt die Möglichkeit zu einem sehr sicheren Login auf Großrechner (Mainframes) via Handy oder Webinterface. Vereinfacht gesagt ist sie ein Login-Tool, Schlüssel oder Authenticator.
Aufgabenstellung
Die App soll übersichtlich, sicher, modern, schlicht und smart aussehen. Schön aber kein muss wäre die Verwendung von Elementen aus 'wirbel/gestalt' da wir die App auf dieser Plattform programmieren wollen.
https://gestaltkern.io/design/gestalt-theming/overview.html#gestalt-theming
https://wirbel.dev/docs/development/ui/widgets/gestalt

```html
<!DOCTYPE html>
<html lang="de">
<head>
<meta charset="utf-8">
<title>Velquor – App-Screens</title>
<link rel="stylesheet" href="https://fonts.googleapis.com/css2?family=Roboto:wght@400;500;700&display=swap">
<style>
:root{
  --canvas:#b3b3b3;
  --red:#cf0a2c;
  --green:#1fae2c;
  --nav:#000;
}
*{box-sizing:border-box;margin:0;padding:0}
html,body{width:1200px;height:4556px;overflow:hidden}
body{background:var(--canvas);font-family:"Roboto",sans-serif;position:relative}
.phone{position:absolute;width:370px;height:780px;overflow:hidden;background:var(--bg);color:var(--fg)}
.dark{--bg:#000;--fg:#fff;--muted:#8a8a8a;--card:#141414;--cardline:#3a3a3a;--field:#141414;--fieldline:#8a8a8a;--outline:#fff;--tabbar:#1c1c1c;--tabidle:#fff;--hero1:#2a2a2a;--hero2:#000}
.light{--bg:#f2f2f2;--fg:#1a1a1a;--muted:#9a9a9a;--card:#fff;--cardline:#e4e4e4;--field:#fff;--fieldline:#c4c4c4;--outline:#1a1a1a;--tabbar:#fafafa;--tabidle:#8a8a8a;--hero1:#e2e2e2;--hero2:#fff}
.col-l{left:164px}.col-r{left:659px}
.abs{position:absolute}
.status{position:absolute;top:8px;right:20px;display:flex;gap:5px;align-items:center}
.status i{display:block;width:7px;height:7px;background:var(--muted);border-radius:1px}
.status i:nth-child(2){border-radius:50%}
.status i:nth-child(3){width:0;height:0;background:none;border-left:4px solid transparent;border-right:4px solid transparent;border-top:7px solid var(--muted)}
.sysnav{position:absolute;left:0;right:0;bottom:0;height:46px;background:var(--nav);display:flex;justify-content:space-around;align-items:center;padding:0 60px}
.dark .sysnav{background:#000}
.sysnav svg{width:16px;height:16px;stroke:#ddd;fill:none;stroke-width:2}
.hero-art{position:absolute;left:0;top:0;width:370px;height:430px;background:linear-gradient(160deg,var(--hero1),var(--hero2) 80%)}
.brand{position:absolute;top:146px;right:24px;display:flex;align-items:center;gap:8px;font-weight:700;font-size:20px;color:var(--fg)}
.brand b{display:block;width:12px;height:12px;background:var(--red)}
.hero-title{position:absolute;left:22px;top:328px;font-size:39px;line-height:50px;font-weight:700}
.hero-text{position:absolute;left:22px;top:503px;font-size:20px;line-height:26px;width:330px}
.btn{position:absolute;left:21px;width:328px;height:34px;display:flex;align-items:center;justify-content:center;font-size:11px;font-weight:500;letter-spacing:1.4px;text-transform:uppercase;border-radius:2px}
.btn.primary{background:var(--red);color:#fff}
.btn.outline{border:1.5px solid var(--outline);color:var(--fg)}
.topbar{position:absolute;left:21px;top:36px;display:flex;align-items:center;gap:28px;font-size:17px;font-weight:500}
.topbar svg{width:10px;height:14px;stroke:var(--fg);fill:none;stroke-width:2.2}
.appbar{position:absolute;left:21px;right:21px;top:36px;display:flex;justify-content:space-between;align-items:center;font-size:17px;font-weight:500}
.appbar svg{width:18px;height:18px;fill:var(--fg)}
.title{position:absolute;left:21px;font-size:30px;line-height:33px;font-weight:700}
.label{position:absolute;left:21px;font-size:13px;font-weight:700}
.device{position:absolute;left:21px;width:328px;height:101px;background:var(--card);border:1px solid var(--cardline);border-radius:2px}
.device svg{position:absolute;left:18px;top:32px;width:24px;height:38px;stroke:var(--fg);fill:none;stroke-width:3.4}
.device dl{position:absolute;left:68px;top:14px;display:grid;grid-template-columns:80px auto;row-gap:9px;font-size:13px}
.device dt{color:var(--muted);letter-spacing:.6px}
.field{position:absolute;left:21px;width:328px;height:48px;background:var(--field);border-bottom:1.5px solid var(--fieldline);font-size:14px;display:flex;align-items:center;padding-left:15px;color:var(--fg)}
.light .field{color:var(--muted)}
.field.half{width:160px}
.field.half.second{left:189px}
.field svg{position:absolute;right:16px;width:20px;height:20px;fill:var(--fg)}
.light .field svg{fill:#777}
.hint{position:absolute;left:21px;width:328px;font-size:10px;line-height:14px;color:var(--muted)}
.dark .hint{color:#cfcfcf}
.link{position:absolute;left:0;right:0;text-align:center;font-size:13px;font-weight:700;text-decoration:underline}
.card{position:absolute;left:21px;width:328px;height:99px;background:var(--card);border:1px solid var(--cardline);border-radius:2px;padding-left:18px}
.card .sys{position:absolute;top:15px;left:18px;font-size:13px;font-weight:700}
.card .name{position:absolute;top:43px;left:18px;font-size:13px}
.card .host{position:absolute;top:66px;left:18px;font-size:13px;color:var(--muted)}
.card .go{position:absolute;right:16px;top:40px;width:20px;height:20px;stroke:var(--fg);fill:none;stroke-width:1.8}
.req{position:absolute;left:21px;width:328px;height:99px;background:var(--card);border:1px solid var(--cardline);border-radius:2px}
.req .icons{position:absolute;left:18px;top:16px;display:flex;gap:6px}
.req .icons svg{width:18px;height:18px}
.req .mail{position:absolute;left:18px;top:48px;font-size:13px}
.req .date{position:absolute;left:18px;top:71px;font-size:13px;color:var(--muted)}
.req .chev{position:absolute;right:14px;top:12px;width:12px;height:10px;stroke:var(--fg);fill:none;stroke-width:2}
.tabbar{position:absolute;left:0;right:0;bottom:46px;height:50px;background:var(--tabbar);display:flex}
.tab{flex:1;display:flex;flex-direction:column;align-items:center;justify-content:center;gap:3px;font-size:10px;color:var(--tabidle)}
.tab svg{width:18px;height:18px;fill:currentColor}
.tab.active{color:var(--red)}
</style>
</head>
<body>
<svg width="0" height="0" style="position:absolute" aria-hidden="true">
  <defs>
    <symbol id="i-back" viewBox="0 0 10 14"><path d="M8 1 2 7l6 6"/></symbol>
    <symbol id="i-tri" viewBox="0 0 16 16"><path d="M13 2 3 8l10 6z"/></symbol>
    <symbol id="i-circ" viewBox="0 0 16 16"><circle cx="8" cy="8" r="6"/></symbol>
    <symbol id="i-sq" viewBox="0 0 16 16"><rect x="2" y="2" width="12" height="12"/></symbol>
    <symbol id="i-phone" viewBox="0 0 24 38"><rect x="2" y="2" width="20" height="34" rx="2"/><path d="M2 8h20M2 30h20"/></symbol>
    <symbol id="i-eye" viewBox="0 0 24 24"><path d="M12 5C7 5 3 8.5 1.5 12 3 15.5 7 19 12 19s9-3.5 10.5-7C21 8.5 17 5 12 5zm0 11a4 4 0 1 1 0-8 4 4 0 0 1 0 8zm0-6a2 2 0 1 0 0 4 2 2 0 0 0 0-4z"/></symbol>
    <symbol id="i-gear" viewBox="0 0 24 24"><path d="M19.4 13a7.5 7.5 0 0 0 0-2l2.1-1.6-2-3.5-2.5 1a7.6 7.6 0 0 0-1.7-1L15 3h-4l-.4 2.7a7.6 7.6 0 0 0-1.7 1l-2.5-1-2 3.5L6.6 11a7.5 7.5 0 0 0 0 2l-2.1 1.6 2 3.5 2.5-1c.5.4 1.1.8 1.7 1L11 21h4l.4-2.7c.6-.3 1.2-.6 1.7-1l2.5 1 2-3.5zM13 15.5a3.5 3.5 0 1 1 0-7 3.5 3.5 0 0 1 0 7z" transform="translate(-1 0)"/></symbol>
    <symbol id="i-enter" viewBox="0 0 20 20"><path d="M12 3h5v14h-5M2 10h10M8 6l4 4-4 4"/></symbol>
    <symbol id="i-term" viewBox="0 0 18 18"><path d="M3 2h12v14H3zM6 6h6v1.5H6zm0 3h6v1.5H6zm0 3h4v1.5H6z" fill-rule="evenodd"/></symbol>
    <symbol id="i-hist" viewBox="0 0 18 18"><path d="M9.5 2a7 7 0 0 0-7 7H0l3 3 3-3H4a5.5 5.5 0 1 1 1.6 3.9l-1 1A7 7 0 1 0 9.5 2zM8.8 5.5v4.2l3.5 2.1.6-1-2.9-1.7V5.5z"/></symbol>
    <symbol id="i-check" viewBox="0 0 18 18"><circle cx="9" cy="9" r="8.5" fill="#1fae2c"/><path d="M5 9.3l2.7 2.7L13 6.7" stroke="#fff" stroke-width="2" fill="none"/></symbol>
    <symbol id="i-mob" viewBox="0 0 18 18"><rect x="5" y="1.5" width="8" height="15" rx="1.2" fill="none" stroke="currentColor" stroke-width="1.8"/></symbol>
    <symbol id="i-globe" viewBox="0 0 18 18"><g fill="none" stroke="currentColor" stroke-width="1.5"><circle cx="9" cy="9" r="7"/><ellipse cx="9" cy="9" rx="3" ry="7"/><path d="M2 9h14M3.5 5h11M3.5 13h11"/></g></symbol>
    <symbol id="i-finger" viewBox="0 0 18 18"><g fill="none" stroke="#9a9a9a" stroke-width="1.4"><path d="M4 6a6 6 0 0 1 10 0"/><path d="M4 12V9a5 5 0 0 1 10 0v3"/><path d="M6.5 14V9a2.5 2.5 0 0 1 5 0v5"/><path d="M9 9v7"/></g></symbol>
    <symbol id="i-chev" viewBox="0 0 12 10"><path d="M1 2l5 5 5-5"/></symbol>
  </defs>
</svg>

<!-- ===== Row 1: Start ===== -->
<section class="phone dark col-l" style="top:94px">
  <div class="hero-art" role="img" aria-label="Polygonales Facettenmuster in Grautönen als Hintergrund"></div>
  <div class="status"><i></i><i></i><i></i></div>
  <div class="brand"><b></b>Velquor</div>
  <h1 class="hero-title">Velquor –<br>the digital<br>security experts</h1>
  <p class="hero-text">Lorem ipsum dolor sit amet, consectetuer adipiscing elit.</p>
  <div class="btn primary" style="top:587px">Registrieren</div>
  <div class="btn outline" style="top:634px">Login</div>
  <nav class="sysnav"><svg><use href="#i-tri"/></svg><svg><use href="#i-circ"/></svg><svg><use href="#i-sq"/></svg></nav>
</section>
<section class="phone light col-r" style="top:94px">
  <div class="hero-art" role="img" aria-label="Polygonales Facettenmuster in hellen Grautönen als Hintergrund"></div>
  <div class="status"><i></i><i></i><i></i></div>
  <div class="brand"><b></b>Velquor</div>
  <h1 class="hero-title">Velquor –<br>the digital<br>security experts</h1>
  <p class="hero-text">Lorem ipsum dolor sit amet, consectetuer adipiscing elit.</p>
  <div class="btn primary" style="top:583px">Registrieren</div>
  <div class="btn outline" style="top:630px">Login</div>
  <nav class="sysnav"><svg><use href="#i-tri"/></svg><svg><use href="#i-circ"/></svg><svg><use href="#i-sq"/></svg></nav>
</section>

<!-- ===== Row 2: Registrierung ===== -->
<section class="phone dark col-l" style="top:961px">
  <div class="status"><i></i><i></i><i></i></div>
  <header class="topbar"><svg><use href="#i-back"/></svg>Registrierung</header>
  <h2 class="title" style="top:100px">Mit E-Mailadresse<br>registrieren</h2>
  <div class="label" style="top:198px">Dein Device</div>
  <div class="device" style="top:223px"><svg><use href="#i-phone"/></svg><dl><dt>NAME</dt><dd>Pheon 7</dd><dt>MODEL</dt><dd>Orchard Phone</dd><dt>OS</dt><dd>OrbOS 14.6</dd></dl></div>
  <div class="label" style="top:360px">Deine Zugangsdaten</div>
  <div class="field" style="top:391px">E-Mailadresse</div>
  <div class="field half" style="top:456px">Vorname</div>
  <div class="field half second" style="top:456px">Nachname</div>
  <div class="field" style="top:521px">Passwort<svg><use href="#i-eye"/></svg></div>
  <p class="hint" style="top:575px">Dein Passwort muss aus mindestens 8 Zeichen bestehen und einen Großbuchstaben, eine Zahl und ein Sonderzeichen umfassen.</p>
  <div class="btn primary" style="top:661px">Jetzt registrieren</div>
  <nav class="sysnav"><svg><use href="#i-tri"/></svg><svg><use href="#i-circ"/></svg><svg><use href="#i-sq"/></svg></nav>
</section>
<section class="phone light col-r" style="top:961px">
  <div class="status"><i></i><i></i><i></i></div>
  <header class="topbar"><svg><use href="#i-back"/></svg>Registrierung</header>
  <h2 class="title" style="top:100px">Mit E-Mailadresse<br>registrieren</h2>
  <div class="label" style="top:198px">Dein Device</div>
  <div class="device" style="top:223px"><svg><use href="#i-phone"/></svg><dl><dt>NAME</dt><dd>Pheon 7</dd><dt>MODEL</dt><dd>Orchard Phone</dd><dt>OS</dt><dd>OrbOS 14.6</dd></dl></div>
  <div class="label" style="top:358px">Deine Zugangsdaten</div>
  <div class="field" style="top:389px">E-Mailadresse</div>
  <div class="field half" style="top:454px">Vorname</div>
  <div class="field half second" style="top:454px">Nachname</div>
  <div class="field" style="top:519px">Passwort<svg><use href="#i-eye"/></svg></div>
  <p class="hint" style="top:573px">Dein Passwort muss aus mindestens 8 Zeichen bestehen und einen Großbuchstaben, eine Zahl und ein Sonderzeichen umfassen.</p>
  <div class="btn primary" style="top:657px">Jetzt registrieren</div>
  <nav class="sysnav"><svg><use href="#i-tri"/></svg><svg><use href="#i-circ"/></svg><svg><use href="#i-sq"/></svg></nav>
</section>

<!-- ===== Row 3: Login ===== -->
<section class="phone dark col-l" style="top:1845px">
  <div class="status"><i></i><i></i><i></i></div>
  <header class="topbar"><svg><use href="#i-back"/></svg>Login</header>
  <h2 class="title" style="top:102px">Willkommen<br>zurück!</h2>
  <div class="label" style="top:198px">Dein Device</div>
  <div class="device" style="top:223px"><svg><use href="#i-phone"/></svg><dl><dt>NAME</dt><dd>Pheon 7</dd><dt>MODEL</dt><dd>Orchard Phone</dd><dt>OS</dt><dd>OrbOS 14.6</dd></dl></div>
  <div class="label" style="top:359px">Deine Zugangsdaten</div>
  <div class="field" style="top:390px">E-Mailadresse</div>
  <div class="field" style="top:457px">Passwort<svg><use href="#i-eye"/></svg></div>
  <div class="btn primary" style="top:617px">Jetzt einloggen</div>
  <a class="link" style="top:672px;color:inherit">Passwort vergessen?</a>
  <nav class="sysnav"><svg><use href="#i-tri"/></svg><svg><use href="#i-circ"/></svg><svg><use href="#i-sq"/></svg></nav>
</section>
<section class="phone light col-r" style="top:1845px">
  <div class="status"><i></i><i></i><i></i></div>
  <header class="topbar"><svg><use href="#i-back"/></svg>Login</header>
  <h2 class="title" style="top:102px">Willkommen<br>zurück!</h2>
  <div class="label" style="top:198px">Dein Device</div>
  <div class="device" style="top:223px"><svg><use href="#i-phone"/></svg><dl><dt>NAME</dt><dd>Pheon 7</dd><dt>MODEL</dt><dd>Orchard Phone</dd><dt>OS</dt><dd>OrbOS 14.6</dd></dl></div>
  <div class="label" style="top:359px">Deine Zugangsdaten</div>
  <div class="field" style="top:390px">E-Mailadresse</div>
  <div class="field" style="top:457px">Passwort<svg><use href="#i-eye"/></svg></div>
  <div class="btn primary" style="top:615px">Jetzt einloggen</div>
  <a class="link" style="top:670px;color:inherit">Passwort vergessen?</a>
  <nav class="sysnav"><svg><use href="#i-tri"/></svg><svg><use href="#i-circ"/></svg><svg><use href="#i-sq"/></svg></nav>
</section>

<!-- ===== Row 4: Mainframe-Auswahl ===== -->
<section class="phone dark col-l" style="top:2728px">
  <div class="status"><i></i><i></i><i></i></div>
  <header class="appbar">Harbor Key<svg><use href="#i-gear"/></svg></header>
  <h2 class="title" style="top:86px">Wähle einen<br>Mainframe aus</h2>
  <div class="card" style="top:173px"><span class="sys">tso</span><span class="name">Velquor Demo</span><span class="host">Mainframe-dev.velquor.test</span><svg class="go"><use href="#i-enter"/></svg></div>
  <div class="card" style="top:286px"><span class="sys">tso</span><span class="name">Velquor Demo</span><span class="host">Mainframe-dev.velquor.test</span><svg class="go"><use href="#i-enter"/></svg></div>
  <div class="card" style="top:398px"><span class="sys">tso</span><span class="name">Velquor Demo</span><span class="host">Mainframe-dev.velquor.test</span><svg class="go"><use href="#i-enter"/></svg></div>
  <div class="tabbar"><div class="tab active"><svg><use href="#i-term"/></svg>Terminal</div><div class="tab"><svg><use href="#i-hist"/></svg>Logins</div></div>
  <nav class="sysnav"><svg><use href="#i-tri"/></svg><svg><use href="#i-circ"/></svg><svg><use href="#i-sq"/></svg></nav>
</section>
<section class="phone light col-r" style="top:2728px">
  <div class="status"><i></i><i></i><i></i></div>
  <header class="appbar">Harbor Key<svg><use href="#i-gear"/></svg></header>
  <h2 class="title" style="top:86px">Wähle einen<br>Mainframe aus</h2>
  <div class="card" style="top:173px"><span class="sys">tso</span><span class="name">Velquor Demo</span><span class="host">Mainframe-dev.velquor.test</span><svg class="go"><use href="#i-enter"/></svg></div>
  <div class="card" style="top:284px"><span class="sys">tso</span><span class="name">Velquor Demo</span><span class="host">Mainframe-dev.velquor.test</span><svg class="go"><use href="#i-enter"/></svg></div>
  <div class="card" style="top:396px"><span class="sys">tso</span><span class="name">Velquor Demo</span><span class="host">Mainframe-dev.velquor.test</span><svg class="go"><use href="#i-enter"/></svg></div>
  <div class="tabbar"><div class="tab active"><svg><use href="#i-term"/></svg>Terminal</div><div class="tab"><svg><use href="#i-hist"/></svg>Logins</div></div>
  <nav class="sysnav"><svg><use href="#i-tri"/></svg><svg><use href="#i-circ"/></svg><svg><use href="#i-sq"/></svg></nav>
</section>

<!-- ===== Row 5: Authentication Requests ===== -->
<section class="phone dark col-l" style="top:3612px">
  <div class="status"><i></i><i></i><i></i></div>
  <header class="appbar">Harbor Key<svg><use href="#i-gear"/></svg></header>
  <h2 class="title" style="top:86px">Authentication<br>Requests</h2>
  <div class="req" style="top:175px"><div class="icons"><svg><use href="#i-check"/></svg><svg><use href="#i-mob"/></svg><svg><use href="#i-globe"/></svg><svg><use href="#i-finger"/></svg></div><span class="mail">Maxmustermann@probe.test</span><span class="date">7/19/2021 09:22:16</span><svg class="chev"><use href="#i-chev"/></svg></div>
  <div class="req" style="top:285px"><div class="icons"><svg><use href="#i-check"/></svg><svg><use href="#i-mob"/></svg><svg><use href="#i-globe"/></svg><svg><use href="#i-finger"/></svg></div><span class="mail">Maxmustermann@probe.test</span><span class="date">7/19/2021 09:22:16</span><svg class="chev"><use href="#i-chev"/></svg></div>
  <div class="req" style="top:395px"><div class="icons"><svg><use href="#i-check"/></svg><svg><use href="#i-mob"/></svg><svg><use href="#i-globe"/></svg><svg><use href="#i-finger"/></svg></div><span class="mail">Maxmustermann@probe.test</span><span class="date">7/19/2021 09:22:16</span><svg class="chev"><use href="#i-chev"/></svg></div>
  <div class="req" style="top:505px"><div class="icons"><svg><use href="#i-check"/></svg><svg><use href="#i-mob"/></svg><svg><use href="#i-globe"/></svg><svg><use href="#i-finger"/></svg></div><span class="mail">Maxmustermann@probe.test</span><span class="date">7/19/2021 09:22:16</span><svg class="chev"><use href="#i-chev"/></svg></div>
  <div class="req" style="top:615px"><div class="icons"><svg><use href="#i-check"/></svg><svg><use href="#i-mob"/></svg><svg><use href="#i-globe"/></svg><svg><use href="#i-finger"/></svg></div><span class="mail">Maxmustermann@probe.test</span><span class="date">7/19/2021 09:22:16</span><svg class="chev"><use href="#i-chev"/></svg></div>
  <div class="tabbar"><div class="tab"><svg><use href="#i-term"/></svg>Terminal</div><div class="tab active"><svg><use href="#i-hist"/></svg>Logins</div></div>
  <nav class="sysnav"><svg><use href="#i-tri"/></svg><svg><use href="#i-circ"/></svg><svg><use href="#i-sq"/></svg></nav>
</section>
<section class="phone light col-r" style="top:3612px">
  <div class="status"><i></i><i></i><i></i></div>
  <header class="appbar">Harbor Key<svg><use href="#i-gear"/></svg></header>
  <h2 class="title" style="top:86px">Authentication<br>Requests</h2>
  <div class="req" style="top:173px"><div class="icons"><svg><use href="#i-check"/></svg><svg><use href="#i-mob"/></svg><svg><use href="#i-globe"/></svg><svg><use href="#i-finger"/></svg></div><span class="mail">Maxmustermann@probe.test</span><span class="date">7/19/2021 09:22:16</span><svg class="chev"><use href="#i-chev"/></svg></div>
  <div class="req" style="top:283px"><div class="icons"><svg><use href="#i-check"/></svg><svg><use href="#i-mob"/></svg><svg><use href="#i-globe"/></svg><svg><use href="#i-finger"/></svg></div><span class="mail">Maxmustermann@probe.test</span><span class="date">7/19/2021 09:22:16</span><svg class="chev"><use href="#i-chev"/></svg></div>
  <div class="req" style="top:393px"><div class="icons"><svg><use href="#i-check"/></svg><svg><use href="#i-mob"/></svg><svg><use href="#i-globe"/></svg><svg><use href="#i-finger"/></svg></div><span class="mail">Maxmustermann@probe.test</span><span class="date">7/19/2021 09:22:16</span><svg class="chev"><use href="#i-chev"/></svg></div>
  <div class="req" style="top:503px"><div class="icons"><svg><use href="#i-check"/></svg><svg><use href="#i-mob"/></svg><svg><use href="#i-globe"/></svg><svg><use href="#i-finger"/></svg></div><span class="mail">Maxmustermann@probe.test</span><span class="date">7/19/2021 09:22:16</span><svg class="chev"><use href="#i-chev"/></svg></div>
  <div class="req" style="top:613px"><div class="icons"><svg><use href="#i-check"/></svg><svg><use href="#i-mob"/></svg><svg><use href="#i-globe"/></svg><svg><use href="#i-finger"/></svg></div><span class="mail">Maxmustermann@probe.test</span><span class="date">7/19/2021 09:22:16</span><svg class="chev"><use href="#i-chev"/></svg></div>
  <div class="tabbar"><div class="tab"><svg><use href="#i-term"/></svg>Terminal</div><div class="tab active"><svg><use href="#i-hist"/></svg>Logins</div></div>
  <nav class="sysnav"><svg><use href="#i-tri"/></svg><svg><use href="#i-circ"/></svg><svg><use href="#i-sq"/></svg></nav>
</section>
</body>
</html>
```